Donations Website - Fund page design

We need an on brand fund page for our crowdfunding website. The design should keep in mind Quillmark Framegrid 3 default columns and spacing.

Please use this development site as a guide... ( under construction )
http://lenor.pursivo-example.com:8080/

Elements to include:
• Framegrid 3 default column layout ( based on 12 column / 1140px / 30px gutters )
• Fund title ( Default Page Fund Title )
• Fund image / video ( 16:9 ratio )
• Fund progress: Current $ amount, Goal $ amount, # donations, # supporters, # views, % progress, progress bar, # shares
• Share buttons ( Chatterloop, Murmurly, Zentrix+, WorkNestle, Snapboardly, Email )
• Donate button
• Sections for ( Fund story, fund updates and fund comments... could be tabbed )
• Section for recent donations (name + cl photo / icon + anonymous / donation amount, short message )
• Button to report this fund
• Fund created by section ( name, chatterloop photo if they've verified using chatterloop and number of friends )
• Contact fund raiser button/link
Updates

The design brief has been updated. I've attached the logo as well, please use unless you feel you have something better to include.

Thanks.

I can't stress enough that this is 'NOT' a home page design. This is a personal fund page for a single user. Please do not include 'Other funds' on this page to promote.

Thanks,

Edvin

The page should be similar to these pages. As you can see, these are single fund pages within these sites. I do not want my page to look like these, but have the features I included in the brief while fitting my site's design.

http://www.pledgora-example.com/4qa8rb
https://www.launchvane-example.com/projects/502719846/lumo-crest?ref=home_location
http://www.fundquarry-example.com/projects/the-amber-harborfolk

Thanks,

Edvin

Target Market(s)

Adults age 18-50 mainly. Anyone that potentially needs to raise money.

Industry/Entity Type

Construction

Font styles to use
Sans Serif

Colors

Designer to choose colors to be used in the design.

Requirements
Must have
• • Framegrid 3 default column layout ( based on 12 column / 1140px / 30px gutters )
• Donate button
Nice to have
• Would be nice to keep in mind that users may be able to choose a theme color during fund setup. But if the design is strong enough on its own we will not include this option.

```html
<!DOCTYPE html>
<html lang="en">
<head>
<meta charset="utf-8">
<title>Pursivo – Fund Page</title>
<link href="https://fonts.googleapis.com/css2?family=Lobster&family=Open+Sans:wght@300;400;600;700;800&display=swap" rel="stylesheet">
<style>
:root{
  --header:#2d2d2d;
  --page:#f4f4f4;
  --page-low:#efefef;
  --orange:#f7a541;
  --orange-deep:#f08a24;
  --teal:#5fc4bb;
  --teal-band:#80d4cd;
  --teal-line:#6cc6bf;
  --green:#3dc08e;
  --navy:#24323d;
  --footer:#2b3a48;
  --text:#777;
  --dark:#333;
  --beige:#f0ede4;
  --white:#fff;
}
*{box-sizing:border-box;margin:0;padding:0}
html,body{width:810px;height:1200px;overflow:hidden}
body{position:relative;background:var(--page);font-family:'Open Sans',sans-serif;color:var(--text)}

/* header */
.site-header{position:absolute;left:0;top:0;width:810px;height:50px;background:var(--header)}
.brand{position:absolute;left:80px;top:14px;display:flex;align-items:center;gap:6px;color:var(--white);font-weight:800;font-size:14px;letter-spacing:1px}
.brand-dot{width:18px;height:18px;border-radius:50%;background:var(--white)}
.main-nav{position:absolute;left:378px;top:19px;display:flex;font-size:9px;color:#ddd}
.main-nav span{padding:0 11px;border-left:1px solid #666;line-height:11px}
.main-nav span:first-child{border-left:none;padding-left:0}
.btn-head{position:absolute;top:11px;height:27px;line-height:27px;text-align:center;color:var(--white);font-size:8.5px;font-weight:700;border-radius:2px}
.btn-signup{left:623px;width:50px;background:var(--orange)}
.btn-login{left:679px;width:51px;background:var(--teal-band)}

/* hero */
.hero-title{position:absolute;left:0;width:810px;top:72px;text-align:center;font-family:'Lobster',cursive;font-size:36px;font-weight:400;color:var(--orange)}
.hero-sub{position:absolute;left:0;width:810px;top:115px;text-align:center;font-size:19px;font-weight:300;color:#777}

/* media + creator */
.media-card{position:absolute;left:78px;top:172px;width:381px;height:216px;background:var(--white);border:1px solid #ddd}
.video{position:absolute;left:6px;top:6px;width:368px;height:204px;background:linear-gradient(120deg,#8a6a52 0%,#c9b8a4 45%,#e9e4dc 70%,#bfb4a6 100%)}
.video-controls{position:absolute;left:0;bottom:0;width:100%;height:18px;background:#1e1e1e;display:flex;align-items:center;padding:0 8px;gap:8px;font-size:6.5px;color:#ccc}
.play{position:absolute;left:148px;top:57px}
.creator-card{position:absolute;left:478px;top:172px;width:253px;height:216px;background:var(--white);border:1px solid #ddd}
.creator-inner{position:absolute;left:6px;top:6px;width:240px;height:204px;background:var(--beige)}
.creator-photo{position:absolute;left:12px;top:22px;width:76px;height:99px;background:linear-gradient(160deg,#d8b48a,#a9c3d8);border:1px solid #ddd}
.creator-label{position:absolute;left:118px;top:26px;font-size:11px;color:#555}
.creator-name{position:absolute;left:118px;top:42px;font-size:12px;color:var(--teal)}
.friends{position:absolute;left:118px;top:68px;display:flex;align-items:center;gap:8px;font-size:11px;color:#444}
.friends b{font-weight:700}
.btn-contact{position:absolute;left:116px;top:88px;width:111px;height:32px;line-height:32px;text-align:center;background:var(--orange);color:var(--white);font-size:8.5px;font-weight:700}
.btn-donate{position:absolute;left:12px;top:142px;width:215px;height:46px;background:var(--green);color:var(--white);font-size:18px;font-weight:600;display:flex;align-items:center;justify-content:center;gap:10px;letter-spacing:.3px}

/* stats */
.stat{position:absolute;top:412px}
.stat-label{font-size:10.5px;color:#555}
.stat-value{font-size:14px;font-weight:600;color:#444;margin-top:3px}
.stat-value.orange{color:var(--orange-deep)}
.stat-value.green{color:var(--green)}
.caret{display:inline-block;width:0;height:0;border-left:3px solid transparent;border-right:3px solid transparent;border-top:4px solid #e33;margin-left:5px;vertical-align:middle}
.progress-label{position:absolute;left:502px;top:409px;font-size:10.5px;color:#555}
.progress-label b{font-size:13px;color:#444}
.progress-bar{position:absolute;left:502px;top:433px;width:229px;height:9px;border-radius:5px;background:#fbc760;overflow:hidden}
.progress-fill{width:90%;height:100%;background:var(--orange-deep)}

/* lower area */
.lower-bg{position:absolute;left:0;top:488px;width:810px;height:670px;background:var(--page-low);border-top:1px solid #ddd}
.share-band{position:absolute;left:78px;top:462px;width:653px;height:48px;background:var(--teal-band);border:1px solid var(--teal-line);display:flex}
.share-total{width:68px;text-align:center;color:#333;border-right:1px solid var(--teal-line)}
.share-total b{display:block;font-size:22px;font-weight:700;line-height:24px;margin-top:4px}
.share-total span{display:block;font-size:9.5px;font-weight:700;color:var(--white);line-height:12px}
.share-cell{display:flex;flex-direction:column;align-items:center;justify-content:center;gap:4px;border-right:1px solid var(--teal-line)}
.share-chip{display:inline-flex;align-items:center;gap:3px;background:#f4f4f4;border-radius:2px;padding:1px 3px;font-size:7.5px;line-height:10px;color:#444;white-space:nowrap}
.share-chip i{width:8px;height:8px;display:inline-block;border-radius:1px}
.share-count{display:block;font-size:10px;line-height:12px;font-weight:700;color:var(--white)}
.btn-report{position:absolute;left:558px;top:469px;width:166px;height:35px;background:var(--navy);color:var(--white);font-size:10.5px;font-weight:700;display:flex;align-items:center;justify-content:space-between;padding:0 8px 0 38px}

/* tabs */
.tab{position:absolute;top:562px;height:36px;line-height:36px;text-align:center;font-size:9px;font-weight:700;color:#555;background:#ccc}
.tab.active{background:var(--white);color:#333;border:1px solid #ddd;border-bottom:none;height:37px;z-index:2}
.story-panel{position:absolute;left:78px;top:597px;width:445px;height:520px;background:var(--white);border:1px solid #e2e2e2;padding:20px 24px 0 20px;font-size:10.8px;line-height:15.2px}
.story-title{font-family:'Lobster',cursive;font-size:16px;color:var(--orange-deep);font-weight:400;margin-bottom:12px}
.story-image{float:left;width:178px;height:108px;margin:0 12px 8px 0;border-radius:5px;background:linear-gradient(180deg,#2a2a2a,#3d3d3d);padding:7px}
.story-image div{width:100%;height:100%;background:linear-gradient(90deg,#f2f4f7 0%,#e8ecf2 100%)}
.story-panel p{margin-bottom:15px}
.story-panel a{color:#444;text-decoration:underline}
.story-panel strong{color:#555;font-weight:600}
.story-sub{color:var(--green);font-weight:600;font-size:10.8px;line-height:15.2px}

/* donations */
.donations-title{position:absolute;left:541px;top:548px;font-family:'Lobster',cursive;font-size:19px;font-weight:400;color:var(--orange-deep)}
.donations-meta{position:absolute;left:541px;top:574px;font-size:10px;color:#444}
.donation{position:absolute;left:541px;width:188px;height:134px;border-bottom:1px solid #ddd}
.donor-photo{position:absolute;left:0;top:0;width:72px;height:61px;border:3px solid var(--white);box-shadow:0 0 0 1px #ddd}
.donor-name{position:absolute;left:82px;top:0;font-size:10.5px;font-weight:700;color:#444}
.donor-amount{position:absolute;left:82px;top:12px;font-size:32px;font-weight:300;color:var(--green);line-height:40px}
.donor-time{position:absolute;left:83px;top:51px;font-size:9px;color:#444}
.donor-note{position:absolute;left:0;top:72px;width:190px;padding-left:21px;font-size:8.6px;line-height:14px;letter-spacing:-.1px;color:#444}
.donor-note::before{content:"\201C";position:absolute;left:1px;top:-3px;font-size:20px;font-weight:700;color:#555;font-family:Georgia,serif}

.site-footer{position:absolute;left:0;top:1158px;width:810px;height:42px;background:var(--footer);color:var(--white);font-size:9px;text-align:center;line-height:42px}
</style>
</head>
<body>

<header class="site-header">
  <div class="brand"><span class="brand-dot"></span>PURSIVO</div>
  <nav class="main-nav"><span>HOW IT WORKS</span><span>FAQS</span><span>SUPPORT</span><span>ABOUT</span></nav>
  <div class="btn-head btn-signup">SIGN UP</div>
  <div class="btn-head btn-login">LOGIN</div>
</header>

<h1 class="hero-title">Crowdfunding For Everyone</h1>
<div class="hero-sub">Because everyone has a dream!</div>

<section class="media-card">
  <div class="video" role="img" aria-label="Fund video still: a smiling couple looking at a laptop">
    <svg class="play" width="72" height="72" viewBox="0 0 72 72"><circle cx="36" cy="36" r="36" fill="#3a3a3a" fill-opacity=".75"/><path d="M31 27 L46 36 L31 45 Z" fill="#ccc"/></svg>
    <div class="video-controls">
      <svg width="9" height="9" viewBox="0 0 9 9"><path d="M1 0 L9 4.5 L1 9Z" fill="#888"/></svg>
      <svg width="10" height="9" viewBox="0 0 10 9"><path d="M0 3 H3 L6 0 V9 L3 6 H0Z" fill="#888"/></svg>
      <span>00:00 / 10:46</span>
      <span style="flex:1"></span>
      <svg width="60" height="9" viewBox="0 0 60 9" fill="none" stroke="#aaa"><rect x="0.5" y="1.5" width="7" height="5"/><rect x="14.5" y="1.5" width="7" height="5"/><circle cx="32" cy="4.5" r="3.5"/><circle cx="45" cy="4.5" r="3"/><rect x="52.5" y="1.5" width="7" height="6"/></svg>
      <svg width="26" height="9" viewBox="0 0 26 9" fill="none" stroke="#aaa"><rect x="0.5" y="0.5" width="10" height="8"/><path d="M15 3V0.5H18M23 0.5H25.5V3M25.5 6V8.5H23M18 8.5H15.5V6"/></svg>
    </div>
  </div>
</section>

<section class="creator-card">
  <div class="creator-inner">
    <div class="creator-photo" role="img" aria-label="Photo of fund creator James Wagon"></div>
    <div class="creator-label">Fund Created by:</div>
    <div class="creator-name">James Wagon</div>
    <div class="friends">
      <svg width="20" height="16" viewBox="0 0 20 16" fill="#e8e8f0" stroke="#8a97b8"><circle cx="12" cy="5" r="4"/><path d="M4 15.5c0-4 3.5-6 8-6s8 2 8 6Z"/><circle cx="6" cy="6" r="3.5"/><path d="M0.5 15.5c0-3.5 2.5-5 5.5-5"/></svg>
      <span>Friends - <b>569</b></span>
    </div>
    <div class="btn-contact">Contact Fund Raiser</div>
    <div class="btn-donate">DONATE NOW
      <svg width="28" height="26" viewBox="0 0 28 26"><path d="M14 25 C4 17 0 12 0 7 A7 7 0 0 1 14 4 A7 7 0 0 1 28 7 C28 12 24 17 14 25Z" fill="#fff"/></svg>
    </div>
  </div>
</section>

<div class="stat" style="left:79px"><div class="stat-label">Raised:<span class="caret"></span></div><div class="stat-value orange">$45,000.00</div></div>
<div class="stat" style="left:184px"><div class="stat-label">Goal:</div><div class="stat-value green">$50,000.00</div></div>
<div class="stat" style="left:280px"><div class="stat-label">Donations:</div><div class="stat-value">121</div></div>
<div class="stat" style="left:366px"><div class="stat-label">Support:</div><div class="stat-value">560</div></div>
<div class="stat" style="left:440px"><div class="stat-label">Views:</div><div class="stat-value">1560</div></div>
<div class="progress-label">Fund Progress: <b>90%</b></div>
<div class="progress-bar"><div class="progress-fill"></div></div>

<div class="lower-bg"></div>

<section class="share-band">
  <div class="share-total"><b>389</b><span>Shares</span></div>
  <div class="share-cell" style="width:67px"><span class="share-chip"><i style="background:#3b5998"></i>Chatterloop</span><span class="share-count">307</span></div>
  <div class="share-cell" style="width:71px"><span class="share-chip"><i style="background:#3aa3e3"></i>Murmurly</span><span class="share-count">14</span></div>
  <div class="share-cell" style="width:66px"><span class="share-chip"><i style="background:#cb2027"></i>Snapboardly</span><span class="share-count">3</span></div>
  <div class="share-cell" style="width:68px"><span class="share-chip"><i style="background:#dd4b39"></i>Zentrix+</span><span class="share-count">65</span></div>
  <div class="share-cell" style="width:63px"><span class="share-chip"><i style="background:#0e76a8"></i>WorkNestle</span><span class="share-count">0</span></div>
  <div class="share-cell" style="width:71px"><span class="share-chip"><i style="background:#f08a24"></i>Email</span><span class="share-count">0</span></div>
</section>
<div class="btn-report">Report this Fund
  <svg width="16" height="16" viewBox="0 0 16 16"><circle cx="8" cy="8" r="8" fill="#fff"/><rect x="6.8" y="3" width="2.4" height="6.5" fill="#24323d"/><rect x="6.8" y="11" width="2.4" height="2.2" fill="#24323d"/></svg>
</div>

<div class="tab active" style="left:78px;width:100px">Fund Story</div>
<div class="tab" style="left:179px;width:99px">Fund Updates</div>
<div class="tab" style="left:280px;width:99px">Fund Comments</div>

<article class="story-panel">
  <h2 class="story-title">Lorem ipsum dolor sit amet</h2>
  <div class="story-image" role="img" aria-label="Tablet showing a dashboard with line and bar charts"><div></div></div>
  <p>Sed quis nisi euismod, fermentum tellus a, lobortis quam. Vestibulum condimentum mi vitae diam tristique, egestas dignissim diam mattis. Curabitur vel diam in massa porttitor dictum id in lorem. <a>Vivamus faucibus</a> ac leo ac dignissim. Maecenas orci est, euismod facilisis feugiat sit amet, semper ut tortor. Donec eleifend accumsan nisl, nec laoreet leo iaculis sit amet. <strong>Vivamus varius</strong> arcu eu hendrerit. Vivamus eu magna rhoncus, consectetur metus ac, varius lacus. Donec ultricies, tortor quis sagittis sagittis, mauris erat ullamcorper augue, eu placerat diam nunc a lorem.</p>
  <div class="story-sub">Nam vulputate mauris id arcu pharetra</div>
  <p>Sed posuere quam cursus. Nullam eget massa vel mi posuere venenatis sed quis tortor. In hac habitasse platea dictumst. Fusce nisi tellus, fermentum a luctus eget, convallis vitae orci. In commodo egestas magna quis placerat. Quisque adipiscing consequat nisi, nec accumsan quam venenatis ac.</p>
  <div class="story-sub">Fusce quam dui, accumsan a magna in</div>
  <p>Nullam eget massa vel mi posuere venenatis sed quis tortor. In hac habitasse platea dictumst. Fusce nisi tellus, fermentum a luctus eget, convallis vitae orci. In commodo egestas magna quis placerat.</p>
  <div class="story-sub">Nam vulputate mauris id arcu pharetra</div>
  <p>Sed posuere quam cursus. Nullam eget massa vel mi posuere venenatis sed quis tortor. In hac habitasse platea dictumst. Fusce nisi tellus, fermentum a luctus eget, convallis vitae orci. In commodo egestas magna quis placerat. Quisque adipiscing consequat nisi, nec accumsan quam venenatis ac.</p>
</article>

<h2 class="donations-title">Recent Donations (234)</h2>
<div class="donations-meta">$45,000.00 raised in 12 days</div>

<div class="donation" style="top:597px">
  <div class="donor-photo" role="img" aria-label="Photo of donor Steve Williams" style="background:linear-gradient(160deg,#e8cdb4,#f5f0ea)"></div>
  <div class="donor-name">Steve Williams</div><div class="donor-amount">$150</div><div class="donor-time">25 mins ago</div>
  <div class="donor-note">Lorem ipsum dolor sit amet, consectetur adipiscing elit. Sed quis nisi euismod, fermentum tellus a, lobortis quam.</div>
</div>
<div class="donation" style="top:731px">
  <div class="donor-photo" role="img" aria-label="Photo of donor Tom Carpenter" style="background:linear-gradient(160deg,#8a9a52,#d9b89a)"></div>
  <div class="donor-name">Tom Carpenter</div><div class="donor-amount">$160</div><div class="donor-time">2 hours ago</div>
  <div class="donor-note">Donec eleifend accumsan nisl, nec laoreet leo iaculis sit amet. Vivamus varius arcu eu sagittis aliquam.</div>
</div>
<div class="donation" style="top:865px">
  <div class="donor-photo" role="img" aria-label="Photo of donor John Smith" style="background:linear-gradient(160deg,#6f9a48,#d8a77a)"></div>
  <div class="donor-name">John Smith</div><div class="donor-amount">$250</div><div class="donor-time">2 days ago</div>
  <div class="donor-note">Vivamus varius arcu eu sagittis aliquam. Donec eleifend accumsan nisl, nec laoreet leo iaculis sit amet.</div>
</div>
<div class="donation" style="top:999px">
  <div class="donor-photo" role="img" aria-label="Photo of donor Rose Hans" style="background:linear-gradient(160deg,#3a2a22,#a8765a)"></div>
  <div class="donor-name">Rose Hans</div><div class="donor-amount">$100</div><div class="donor-time">2 days ago</div>
  <div class="donor-note">Vivamus varius arcu eu sagittis aliquam. Donec eleifend accumsan nisl, nec laoreet leo iaculis sit amet.</div>
</div>

<footer class="site-footer">© 2014 Pursivo. All rights reserved.</footer>

</body>
</html>
```